Web Design Job: Facial Surgery Center (Velantra)--Web Design Needed

We need a web design for Velantra Facial Surgery. Velantra is in Chesterfield, MO (suburb of St. Louis), and is owned by a double board certified facial plastic surgeon and ENT. The website must feature a before and after photo book, a section for patient reviews, drop down menus that outline services offered (one for surgical procedures and one for office/nonsurgical procedures), and "About the Practice" section, a section to talk about the doctor and his staff, a "What's New" section, a section for information for out of town patients, as well as a link to the Medical Spa also owned by the doctor, as well as Facebook and Twitter. We are open to ideas regarding adding a "tour of the surgery center", featuring video footage of the state of the art facility, as well as other video options. We prefer soothing colors such as aquas and blues, light greys, chocolate browns, etc (does not have to follow the color scheme in the attached logo). We would like the design to be easy to digest and informative, but not "thick". It should be an upscale, classy design that will appeal to all age brackets, but especially middle-aged women, as that is the primary clientele.

Target Market(s)

Middle aged women are our most common client, however, younger patients, both male and female, will often visit the site for select procedures.

Industry/Entity Type

Medical

Number of Pages Required

5+ page

Font styles to use
Sans Serif

Colors
86cfc6
85cae6
cee9f5
cfeae6
edf8f6
85acd3
cfdfed

Requirements
Must have
• Before and after picture book, links to Facebook, Twitter and Instagram, a soothing, peaceful aesthetic, a page for reviews, as well as a link to reviews on Yelp or similar page.
Nice to have
• Drop down menus that include the surgical and nonsurgical procedures. Each surgical procedure could have it's own section that includes a before and after picture book.
Should not have
• Too many words!

```html
<!DOCTYPE html>
<html lang="en">
<head>
<meta charset="utf-8">
<title>Velantra Facial Surgery</title>
<link href="https://fonts.googleapis.com/css2?family=Andada+Pro:wght@400;600;700&display=swap" rel="stylesheet">
<style>
:root{
  --sky:#b2dff1;
  --nav:#5ea4c4;
  --nav-active:#4a88aa;
  --navy:#3e6891;
  --slate:#6d8eb3;
  --ink:#4d6f93;
  --aqua:#86cfc6;
  --teal-text:#3e9fa0;
  --contact:#7cc3dc;
  --field:#cfdfed;
  --field-line:#9fc1dc;
  --body:#555b60;
  --white:#ffffff;
  --rule:#e2e4e6;
}
*{box-sizing:border-box;margin:0;padding:0}
html,body{width:1200px;height:1200px;overflow:hidden;background:var(--white)}
body{position:relative;font-family:"Andada Pro",Georgia,serif;color:var(--body)}
.abs{position:absolute}

.brand{left:165px;top:22px;color:var(--navy);font-weight:400}
.brand-name{font-size:34px;letter-spacing:2px;line-height:1}
.brand-sub{font-size:10px;letter-spacing:7px;margin-top:8px}

.social{left:903px;top:17px;display:flex;gap:5px}
.social span{width:25px;height:25px;border-radius:50%;background:var(--contact);display:block}
.contact{right:180px;top:51px;text-align:right;color:var(--contact);font-size:12px;line-height:17px;white-space:nowrap}

.nav{left:160px;top:104px;width:880px;height:35px;background:var(--nav);border-radius:3px 3px 0 0;font-size:10.8px;color:var(--white);text-transform:uppercase;white-space:nowrap}
.nav a{position:absolute;top:0;line-height:35px;color:inherit;text-decoration:none}
.nav a.active{left:0;width:64px;text-align:center;background:var(--nav-active);border-radius:3px 0 0 0}

.band-hero{left:0;top:139px;width:1200px;height:361px;background:var(--sky)}
.hero{left:160px;top:153px;width:880px;height:331px;background:var(--white);border-radius:3px}
.hero-photo{left:164px;top:157px;width:631px;height:323px;background:linear-gradient(115deg,#e9edf0 0%,#cfd8dd 45%,#7fb9c2 70%,#d9dfe3 100%)}
.hero-caption{left:164px;top:354px;width:376px;height:85px;background:rgba(255,255,255,.82);padding:10px 17px}
.hero-caption h1{font-size:23px;font-weight:400;color:#5d6369;line-height:1.2;white-space:nowrap}
.hero-caption p{font-size:9.5px;line-height:14px;margin-top:5px;width:360px;color:#6a6f74}

.appt-title{left:818px;top:166px;font-size:13.5px;display:flex;align-items:center;gap:7px;text-transform:uppercase;color:#5c93bd;white-space:nowrap}
.field{background:var(--field);border:1px solid var(--field-line);border-radius:2px;font-size:9.5px;color:#7a8da0;padding:13px 9px;font-family:Arial,sans-serif}
.submit{left:806px;top:441px;width:226px;height:37px;background:var(--navy);color:var(--white);font-size:22px;font-weight:600;text-align:center;line-height:37px;letter-spacing:.5px;border-radius:2px}

.tour-title{left:162px;top:521px;font-size:20px;color:var(--ink);font-weight:400;white-space:nowrap}
.tour-title b{font-weight:600}
.tour-text{left:162px;top:552px;width:620px;font-size:9.5px;line-height:14px;color:#5a82aa}
.btn-video{left:161px;top:588px;width:170px;height:41px;background:var(--slate);color:var(--white);font-size:11px;display:flex;align-items:center;gap:7px;padding-left:11px;border-radius:2px;text-transform:uppercase;white-space:nowrap}
.video-frame{left:833px;top:517px;width:206px;height:118px;background:var(--white);border:1px solid var(--rule);padding:4px;box-shadow:0 1px 2px rgba(0,0,0,.08)}
.video-frame div{width:100%;height:100%;background:linear-gradient(90deg,#8a7a6e,#c8c6bd 40%,#5d5f67 70%,#b26a4f);position:relative}
.video-frame svg{position:absolute;left:69px;top:31px}
.rule{left:0;top:648px;width:1200px;height:7px;background:var(--rule)}

.card{top:678px;width:193px}
.card-photo{width:193px;height:186px;border:1px solid #d6d9db;border-radius:3px;padding:4px;background:var(--white);box-shadow:0 1px 2px rgba(0,0,0,.1)}
.card-photo div{width:100%;height:100%}
.card h3{font-size:15.5px;font-weight:400;color:var(--teal-text);margin-top:10px}
.card p{font-size:10px;line-height:14px;margin-top:10px;width:190px}
.card .more{display:block;width:80px;height:24px;background:var(--aqua);color:var(--white);font-size:9.5px;text-align:center;line-height:24px;margin-top:10px;text-transform:uppercase}

.band-gallery{left:0;top:1007px;width:1200px;height:193px;background:var(--sky)}
.gallery-title{left:160px;top:1026px;font-size:23px;font-weight:600;color:var(--ink);white-space:nowrap}
.gallery-text{left:161px;top:1068px;width:460px;font-size:9.8px;line-height:13.5px;color:#4e6f8f}
.gallery-text p+p{margin-top:13px}
.btn-gallery{top:1171px;height:32px;font-size:11.5px;text-transform:uppercase;line-height:30px;text-align:center;white-space:nowrap}
.btn-solid{left:162px;width:131px;background:var(--navy);color:var(--white);border:1px solid var(--navy)}
.btn-outline{left:303px;width:140px;border:2px solid var(--navy);color:var(--navy)}
.ba-frame{left:710px;top:1029px;width:329px;height:190px;background:var(--white);border:1px solid #dde;padding:5px}
.ba-frame .pane{position:absolute;top:5px;width:157px;height:190px}
.ba-frame .label{position:absolute;top:5px;background:rgba(255,255,255,.8);font-size:14px;color:#333;padding:3px 10px}
</style>
</head>
<body>

<div class="abs brand">
  <div class="brand-name">Velantra</div>
  <div class="brand-sub">FACIAL SURGERY</div>
</div>

<div class="abs social" aria-label="Social links"><span></span><span></span><span></span><span></span></div>
<div class="abs contact">Call us directly: 314 555 0192<br>4200 Linden Park Dr. Suite 210, Chesterfield, MO.</div>

<nav class="abs nav">
  <a class="active">Home</a>
  <a style="left:74px">Facial Procedures</a>
  <a style="left:220px">Office/Nonsurgical Procedures</a>
  <a style="left:454px">Our Practice</a>
  <a style="left:564px">Contact Information</a>
  <a style="left:734px">Photo Gallery</a>
</nav>

<div class="abs band-hero"></div>
<div class="abs hero"></div>
<div class="abs hero-photo" role="img" aria-label="Smiling clinician in the foreground with a surgeon treating a patient in a bright clinic"></div>
<div class="abs hero-caption">
  <h1>A Passion For Excellence</h1>
  <p>Dr. Hollis artistically and compassionately treats the aging face with surgical enhancements such as face, brow and neck lifts, eyelid surgery as well</p>
</div>

<div class="abs appt-title">
  <svg width="18" height="18" viewBox="0 0 18 18"><rect x="1" y="3" width="16" height="14" rx="1" fill="none" stroke="#5c93bd" stroke-width="2"/><rect x="1" y="3" width="16" height="4" fill="#5c93bd"/><rect x="4" y="0" width="2" height="4" fill="#5c93bd"/><rect x="12" y="0" width="2" height="4" fill="#5c93bd"/><g fill="#5c93bd"><rect x="4" y="9" width="2" height="2"/><rect x="8" y="9" width="2" height="2"/><rect x="12" y="9" width="2" height="2"/><rect x="4" y="13" width="2" height="2"/><rect x="8" y="13" width="2" height="2"/></g></svg>
  Make an Appointment
</div>
<div class="abs field" style="left:805px;top:195px;width:228px;height:35px">Full Name:</div>
<div class="abs field" style="left:805px;top:232px;width:228px;height:35px">Email:</div>
<div class="abs field" style="left:805px;top:270px;width:228px;height:35px">Appoinment For:</div>
<div class="abs field" style="left:805px;top:307px;width:101px;height:35px">Phone No.</div>
<div class="abs field" style="left:909px;top:307px;width:124px;height:35px">Date:</div>
<div class="abs field" style="left:805px;top:345px;width:228px;height:92px;padding-top:11px">Message:</div>
<div class="abs submit">SUBMIT</div>

<h2 class="abs tour-title">Tour of the <b>surgery center</b></h2>
<p class="abs tour-text">Lorem Ipsum is simply dummy text of the printing and typesetting industry. Lorem Ipsum has been the industry's standard dummy text ever since the 1500s, when an unknown printer.Lorem Ipsum is simply dummy text of the printing and typesetting industry.</p>
<div class="abs btn-video">
  <svg width="13" height="13" viewBox="0 0 13 13"><circle cx="6.5" cy="6.5" r="6.5" fill="#fff"/><path d="M5 3.8v5.4l4.2-2.7z" fill="#6d8eb3"/></svg>
  Watch the our video
</div>
<div class="abs video-frame">
  <div role="img" aria-label="Video still of the clinic team standing together in the office">
    <svg width="52" height="52" viewBox="0 0 52 52"><circle cx="26" cy="26" r="23" fill="rgba(0,0,0,.15)" stroke="#fff" stroke-width="4"/><path d="M20 15v22l17-11z" fill="#fff"/></svg>
  </div>
</div>
<div class="abs rule"></div>

<div class="abs card" style="left:160px">
  <div class="card-photo"><div role="img" aria-label="Close profile of a nose and lips" style="background:linear-gradient(120deg,#fff 0%,#f2dccd 45%,#e2b79e 100%)"></div></div>
  <h3>Nose Surgery</h3>
  <p>Lorem Ipsum is simply dummy text of the printing and typesetting industry.</p>
  <span class="more">Read more</span>
</div>
<div class="abs card" style="left:387px">
  <div class="card-photo"><div role="img" aria-label="Portrait of a woman with long brown hair" style="background:linear-gradient(90deg,#6b4a34,#e6c2a6 35%,#eccbb0 60%,#6a4a35)"></div></div>
  <h3>Forehead lift</h3>
  <p>Lorem Ipsum is simply dummy text of the printing and typesetting industry.</p>
  <span class="more">Read more</span>
</div>
<div class="abs card" style="left:616px">
  <div class="card-photo"><div role="img" aria-label="Woman having her ear examined by gloved hands" style="background:linear-gradient(90deg,#fbfbfb,#efd2bf 45%,#f3f3f6 65%,#8e96ea 100%)"></div></div>
  <h3>Ear Surgery</h3>
  <p>Lorem Ipsum is simply dummy text of the printing and typesetting industry.</p>
  <span class="more">Read more</span>
</div>
<div class="abs card" style="left:847px">
  <div class="card-photo"><div role="img" aria-label="Hand resting on a smooth neck" style="background:linear-gradient(100deg,#c9a08e,#e7c2ae 45%,#c08f7f 65%,#6b87a1 100%)"></div></div>
  <h3>Neck Surgery</h3>
  <p>Lorem Ipsum is simply dummy text of the printing and typesetting industry.</p>
  <span class="more">Read more</span>
</div>

<div class="abs band-gallery"></div>
<h2 class="abs gallery-title">Before and after Gallery</h2>
<div class="abs gallery-text">
  <p>Lorem Ipsum is simply dummy text of the printing and typesetting industry. Lorem Ipsum has been the industry's standard dummy text ever since the 1500s, when an unknown printer took a galley of type and scrambled it to make a type specimen book.</p>
  <p>Lorem Ipsum is simply dummy text of the printing and typesetting industry. Lorem Ipsum has been the industry's standard dummy text ever since the 1500s</p>
</div>
<div class="abs btn-gallery btn-solid">See the gallery</div>
<div class="abs btn-gallery btn-outline">Read the reviews</div>
<div class="abs ba-frame">
  <div class="pane" role="img" aria-label="Before photo of a patient" style="left:5px;background:linear-gradient(90deg,#dfe2ea,#2a2526 30%,#e7c8b4 50%,#2a2526 75%,#dfe2ea)"></div>
  <div class="pane" role="img" aria-label="After photo of the same patient" style="left:167px;background:linear-gradient(90deg,#8a8a7e,#1e1a1a 35%,#edc7b0 55%,#1e1a1a 80%,#6f6b63)"></div>
  <span class="label" style="left:5px">BEFORE</span>
  <span class="label" style="left:172px">AFTER</span>
</div>

</body>
</html>
```